Volunteer fire fighters needed banner

As part of our recruitment campaign, we need a sign we can post on our sign trailer to entice locals to join our volunteer fire service. This design will be printed on a banner, front and back, to catch traffic going in both directions on a busy roadway. This banner will have a printed surface of 4 feet tall by 8 feet long.
Our fire department is looking to attract people between the ages of 18 and 35 years old who are interested in being a firefighter. We offer our volunteers:
-Free professional training
-All equipment supplied
-Tax abatements for active volunteers
For more information, you can check us out at:
Brookmerecrestfire.example

This design should:
-scale to and fit a 4'x8' canvas
-Include our web address "BrookmereCrestFire.example"
-Say "Members Wanted"
-"Drill every Tuesday at 7pm"
-"37 Quarry Bend Lane"
-Include "Brookmere Crest Fire Department"

We've included reference photos and past images we use for our other campaigns for inspiration for you.

Target Market(s)

18-35 y/o

Industry/Entity Type

Fire Service

Requirements
Must have
• -scale to and fit a 4'x8' canvas -Include our web address "BrookmereCrestFire.example" -Say "Members Wanted" -"Drill every Tuesday at 7pm" -"37 Quarry Bend Lane" -Include "Brookmere Crest Fire Department"

```html
<!DOCTYPE html>
<html lang="en">
<head>
<meta charset="utf-8">
<title>Members Wanted – Brookmere Crest Fire Department</title>
<link rel="stylesheet" href="https://fonts.googleapis.com/css2?family=Exo+2:ital,wght@1,800;1,900&family=Montserrat:wght@800&display=swap">
<style>
  :root{
    --navy:#33406f;
    --navy-mid:#4a5889;
    --navy-light:#6a78a2;
    --gold:#e6ad2f;
    --white:#ffffff;
    --page:#ffffff;
    --rule:#555555;
    --label:#222222;
  }
  html,body{margin:0;padding:0;overflow:hidden;background:var(--page);}
  .canvas{position:relative;width:1200px;height:2440px;overflow:hidden;background:var(--page);}
  .dimension{position:absolute;left:0;top:0;}
  .dim-label{position:absolute;font-family:"Montserrat",sans-serif;font-weight:800;font-size:28px;color:var(--label);}
  .dim-width{left:606px;top:858px;}
  .dim-height{left:6px;top:1200px;transform:rotate(-90deg);}
  .banner{
    position:absolute;left:80px;top:950px;width:1080px;height:540px;overflow:hidden;
    background:var(--navy);
  }
  .photo{
    position:absolute;left:0;top:0;width:1080px;height:540px;
    background:linear-gradient(180deg,var(--navy) 0%,var(--navy-mid) 45%,var(--navy-light) 70%,var(--navy) 100%);
  }
  .dept-name{
    position:absolute;left:36px;top:26px;margin:0;
    font-family:"Exo 2",sans-serif;font-style:italic;font-weight:800;font-size:30px;line-height:1.1;
    color:var(--gold);text-transform:uppercase;letter-spacing:1px;
  }
  .headline{
    position:absolute;left:0;width:1080px;top:84px;margin:0;text-align:center;
    font-family:"Exo 2",sans-serif;font-style:italic;font-weight:900;font-size:96px;line-height:1.05;
    color:var(--white);letter-spacing:3px;text-transform:uppercase;white-space:nowrap;
  }
  .details{
    position:absolute;left:0;width:1080px;margin:0;text-align:center;
    font-family:"Exo 2",sans-serif;font-style:italic;font-weight:900;font-size:50px;line-height:1.1;
    color:var(--gold);letter-spacing:2px;text-transform:uppercase;white-space:nowrap;
  }
  .drill{top:222px;}
  .address{top:294px;}
  .web-band{
    position:absolute;left:0;top:400px;width:1080px;height:90px;background:var(--gold);
    display:flex;align-items:center;justify-content:center;
  }
  .web-address{
    font-family:"Montserrat",sans-serif;font-weight:800;font-size:42px;color:var(--navy);
    letter-spacing:2px;text-transform:uppercase;
  }
</style>
</head>
<body>
<div class="canvas">
  <svg class="dimension" width="1200" height="2440" viewBox="0 0 1200 2440" aria-hidden="true">
    <g stroke="var(--rule)" stroke-width="1.5" fill="none">
      <line x1="80" y1="905" x2="1160" y2="905"/>
      <line x1="80" y1="885" x2="80" y2="925"/>
      <line x1="1160" y1="885" x2="1160" y2="925"/>
      <line x1="70" y1="915" x2="90" y2="895"/>
      <line x1="1150" y1="915" x2="1170" y2="895"/>
      <line x1="50" y1="950" x2="50" y2="1490"/>
      <line x1="30" y1="950" x2="70" y2="950"/>
      <line x1="30" y1="1490" x2="70" y2="1490"/>
      <line x1="40" y1="940" x2="60" y2="960"/>
      <line x1="40" y1="1480" x2="60" y2="1500"/>
    </g>
  </svg>
  <div class="dim-label dim-width">8′</div>
  <div class="dim-label dim-height">4′</div>

  <section class="banner">
    <div class="photo" role="img" aria-label="Photo of a volunteer firefighter in helmet, breathing mask and turnout gear"></div>
    <p class="dept-name">Brookmere Crest Fire Department</p>
    <h1 class="headline">Members Wanted</h1>
    <p class="details drill">Drill every Tuesday at 7pm</p>
    <p class="details address">37 Quarry Bend Lane</p>
    <div class="web-band"><span class="web-address">BrookmereCrestFire.example</span></div>
  </section>
</div>
</body>
</html>
```